Dating Coach needs a Book Cover Design

My new book called "Where the Lanterns Gather: Meeting Someone Worth Knowing in a Crowded Digital Age" needs a cover! I tried to make one on my own, but it's just not my skill set :) Please see attached for my best attempt. I'd like to see the title smaller and the tagline bigger - so that the tagline is easier to read. But I'm not sure how to do this and still have the Title look great. I'm also considering if the "WHERE LANTERNS GATHER" part should not be in all caps. Looking forward to your ideas! I'm also afraid that the drawing is a bit too cartoonish and doesn't match my brand. I'm looking for something elegant and also very approachable and down to earth. My website is www.gretavondlecounsel.example so you can use as reference! Please see my attached brand style guide for colors. This will be an e-book that I give away for free to anyone who signs up for my newsletter. Some mock-ups would also be great to use in advertising.

```html
<!DOCTYPE html>
<html lang="en">
<head>
<meta charset="utf-8">
<title>Where the Lanterns Gather — Book Cover</title>
<link rel="stylesheet" href="https://fonts.googleapis.com/css2?family=Bodoni+Moda:wght@400&family=Cinzel:wght@600;700&display=swap">
<style>
  :root {
    --paper: #f6f6f5;
    --paper-shade: #ececea;
    --ink: #1c1a1a;
    --plum: #785a8a;
    --olive: #7a6530;
    --dot: #b9ad84;
    --band: #7a5a88;
    --band-text: #ffffff;
    --straw-light: #d9b06a;
    --straw-mid: #b98a3e;
    --straw-dark: #7d5a26;
  }
  * { margin: 0; padding: 0; box-sizing: border-box; }
  html, body { width: 800px; height: 1200px; overflow: hidden; }
  body { background: var(--paper); }

  .cover {
    position: relative;
    width: 800px;
    height: 1200px;
    background: linear-gradient(180deg, var(--paper) 0%, #f3f3f2 60%, var(--paper-shade) 100%);
    text-align: center;
    overflow: hidden;
  }

  .tagline {
    position: absolute;
    top: 92px; left: 0; width: 100%;
    font-family: "Bodoni Moda", serif;
    font-weight: 400;
    font-size: 50px;
    color: var(--ink);
    letter-spacing: 0.5px;
  }

  .divider {
    position: absolute;
    top: 158px; left: 50%;
    transform: translateX(-50%);
  }

  .title {
    position: absolute;
    left: 0; width: 100%;
    font-family: "Cinzel", serif;
    font-weight: 700;
    line-height: 1;
  }
  .title--primary { color: var(--plum); font-size: 84px; }
  .title--line1 { top: 176px; }
  .title--line2 { top: 254px; }

  .subtitle {
    position: absolute;
    top: 350px; left: 0; width: 100%;
    font-family: "Cinzel", serif;
    font-weight: 700;
    font-size: 27px;
    color: var(--ink);
    line-height: 1;
  }

  .title--accent {
    top: 384px;
    color: var(--olive);
    font-size: 84px;
  }

  .cover-art {
    position: absolute;
    left: 130px; top: 500px;
    width: 520px; height: 460px;
    border-radius: 48% 52% 40% 44% / 52% 50% 44% 42%;
    background: radial-gradient(ellipse at 45% 45%, var(--straw-light) 0%, var(--straw-mid) 55%, var(--straw-dark) 85%, rgba(125,90,38,0) 100%);
  }

  .author-band {
    position: absolute;
    left: 0; bottom: 0;
    width: 100%; height: 137px;
    background: var(--band);
    display: flex;
    align-items: center;
    justify-content: center;
  }
  .author-name {
    font-family: "Cinzel", serif;
    font-weight: 600;
    font-size: 52px;
    letter-spacing: 4px;
    color: var(--band-text);
  }
</style>
</head>
<body>
  <main class="cover">
    <p class="tagline">Where the lanterns gather</p>

    <svg class="divider" width="70" height="8" viewBox="0 0 70 8" aria-hidden="true">
      <g fill="var(--dot)">
        <circle cx="5" cy="4" r="3"/><circle cx="17" cy="4" r="3"/><circle cx="29" cy="4" r="3"/>
        <circle cx="41" cy="4" r="3"/><circle cx="53" cy="4" r="3"/><circle cx="65" cy="4" r="3"/>
      </g>
    </svg>

    <h1>
      <span class="title title--primary title--line1">MEETING</span>
      <span class="title title--primary title--line2">SOMEONE</span>
      <span class="subtitle">WORTH KNOWING IN A CROWDED</span>
      <span class="title title--accent">DIGITAL AGE</span>
    </h1>

    <div class="cover-art" role="img" aria-label="Photograph of a round hay bale with a small red heart tucked among the straw"></div>

    <footer class="author-band">
      <p class="author-name">GRETA VONDLE</p>
    </footer>
  </main>
</body>
</html>
```